Run Far Ahead Training Web Design and Launch!

A recently new business in Personal Coaching (Fitness) looking to have a professional website built along with using Zentrix system for payments. Ability to set up memberships would be great. Current site is www.rfatrain.example . I used that site to quickly put something together so that I could get started. Also looking to do something similar to www.morvelgym.example with a shop as well as challenges and leaderboards that members and non members alike can participate in. Would like to have a "meet the coaches" page option along with what I currently have on the site.

Target Market(s)

Men and Women 24-60 years old. Weight loss clients

Industry/Entity Type

Fitness

Coding

Coded - Design and coding required

Number of Pages Required

5+ page

Font styles to use
Sans Serif

Colors
33a6d7
f78f20
0255a3
0592cd

Requirements
Must have
• Zentrix or Payment integration. Photo gallery. Reviews page. Calender link for events. Donation location for Stride4AllKO
Nice to have
• Would like to have a page dedicated to challenges/leaderboards. A way for members and non members to input their results of a posted challenge. Like to have similar pages that my current site www.rfatrain.example has. Ways to sign up for a membership. Meet the coaches and athletes. Gallery designed to call out award winning performances (podium or series wins), Meet the coaches and athletes.

```html
<!DOCTYPE html>
<html lang="en">
<head>
<meta charset="utf-8">
<title>Run Far Ahead Training</title>
<link rel="stylesheet" href="https://fonts.googleapis.com/css2?family=Saira:wght@600;700&family=Roboto:wght@400;500;700&family=Open+Sans:wght@400&display=swap">
<style>
:root{
  --navy:#0a3f94;
  --blue:#0255a3;
  --sky:#2f9bd6;
  --sky-light:#33a6d7;
  --orange:#f78f20;
  --orange-deep:#f07a19;
  --ink:#333;
  --muted:#666;
  --line:#ddd;
  --white:#fff;
}
*{box-sizing:border-box;margin:0;padding:0}
html,body{width:1200px;height:4172px;overflow:hidden;background:var(--white)}
body{position:relative;font-family:"Roboto",sans-serif;color:var(--ink)}
.abs{position:absolute}
.heading{font-family:"Saira",sans-serif;font-weight:700;letter-spacing:1px;text-transform:uppercase}

/* header */
.site-header{left:0;top:0;width:1200px;height:107px;background:var(--white)}
.brand{left:76px;top:20px;display:flex;align-items:center;gap:8px;white-space:nowrap}
.brand-dot{width:66px;height:66px;border-radius:50%;background:var(--blue);flex:none}
.brand-name{font-family:"Saira",sans-serif;font-weight:700;font-size:23px;color:var(--blue);letter-spacing:0}
.main-nav{left:411px;top:45px;display:flex;gap:30px;font-size:14px;font-weight:500;color:#222;text-transform:uppercase;white-space:nowrap}
.main-nav .active{color:var(--sky)}
.btn-member{left:1036px;top:35px;width:132px;height:38px;background:var(--sky);color:var(--white);font-size:14px;font-weight:500;display:flex;align-items:center;justify-content:center}

/* hero */
.hero{left:0;top:107px;width:1200px;height:601px;background:linear-gradient(100deg,#4a6f95 0%,#8a8c88 45%,#b8ad9a 100%)}
.hero-arrow{top:375px;width:30px;height:44px}
.hero-badge{left:122px;top:195px;width:404px;height:404px;border-radius:50%;background:rgba(31,128,204,.9);border:8px solid rgba(255,255,255,.15);text-align:center;color:var(--white)}
.hero-badge h1{font-size:50px;line-height:1.05;margin-top:108px}
.hero-badge p{font-family:"Saira",sans-serif;font-weight:700;font-size:21px;margin-top:14px;letter-spacing:.5px}
.btn-orange{background:var(--orange-deep);color:var(--white);border-radius:28px;font-weight:700;text-transform:uppercase;display:inline-flex;align-items:center;justify-content:center}
.hero-badge .btn-orange{width:196px;height:50px;font-size:17px;margin-top:22px}

/* who we are */
.section-title{width:1200px;left:0;text-align:center;color:var(--blue);font-size:37px}
.intro{left:210px;width:780px;top:834px;text-align:center;font-family:"Open Sans",sans-serif;font-size:16.5px;line-height:27px;color:var(--muted)}
.feature{top:997px;width:331px;height:233px;color:var(--white);text-align:center}
.feature.navy{left:92px;background:var(--blue)}
.feature.sky{left:441px;background:var(--sky)}
.feature.orange{left:789px;background:var(--orange-deep)}
.feature-icon{position:absolute;left:120px;top:-38px;width:91px;height:91px;border-radius:50%;background:var(--white);display:flex;align-items:center;justify-content:center}
.feature h3{font-family:"Roboto",sans-serif;font-weight:700;font-size:20px;line-height:25px;margin-top:74px}
.feature p{font-size:12.5px;line-height:19px;padding:0 42px;margin-top:10px}
.feature-toggle{position:absolute;left:147px;bottom:-19px;width:37px;height:37px;border-radius:50%;background:var(--white);display:flex;align-items:center;justify-content:center}

/* coaches */
.coaches-band{left:0;top:1345px;width:1200px;height:506px;background:linear-gradient(180deg,#8fb9e8 0%,#6fa3de 55%,#3d4350 100%)}
.coaches-badge{left:645px;top:1393px;width:404px;height:404px;border-radius:50%;background:rgba(35,140,208,.92);border:8px solid rgba(255,255,255,.15);text-align:center;color:var(--white)}
.coaches-badge h2{font-size:34px;margin-top:100px}
.coaches-badge p{font-size:15.5px;line-height:25px;padding:0 48px;margin-top:12px}
.btn-outline{display:inline-flex;width:172px;height:44px;border:2px solid var(--white);border-radius:24px;align-items:center;justify-content:center;font-size:14.5px;font-weight:700;margin-top:24px}

/* gallery */
.gallery{left:49px;top:1990px;width:1102px;display:grid;grid-template-columns:repeat(4,269px);grid-auto-rows:244px;gap:8px 8px}
.gallery div:nth-child(1){background:linear-gradient(160deg,#5a5a5a,#2e2e2e)}
.gallery div:nth-child(2){background:linear-gradient(180deg,#2f5eaa,#2a2a30)}
.gallery div:nth-child(3){background:linear-gradient(180deg,#c9c9c9,#3a3838)}
.gallery div:nth-child(4){background:linear-gradient(180deg,#b9b9b9,#4a5060)}
.gallery div:nth-child(5){background:linear-gradient(180deg,#3d4460,#2b2a2c)}
.gallery div:nth-child(6){background:linear-gradient(180deg,#8aa8c4,#4b7fc7)}
.gallery div:nth-child(7){background:linear-gradient(180deg,#7a8c70,#3f6d3a)}
.gallery div:nth-child(8){background:linear-gradient(180deg,#9a9a9a,#4a4a4a)}

/* reviews */
.reviews{left:0;top:2558px;width:1200px;height:429px;background:linear-gradient(180deg,#f07a19,#ee7b1c);color:var(--white)}
.reviews h2{position:absolute;left:0;width:1200px;top:72px;text-align:center;font-size:36px}
.review-avatar{position:absolute;left:236px;top:162px;width:146px;height:146px;border-radius:50%;border:6px solid var(--white);background:linear-gradient(180deg,#d8d2c8,#5a4b86)}
.quote-mark{position:absolute;left:396px;top:150px;font-family:Georgia,serif;font-size:90px;line-height:1;opacity:.7}
.review-text{position:absolute;left:473px;top:152px;width:500px;font-size:19px;line-height:28px}
.reviewer{position:absolute;left:473px;top:283px;font-size:22px;font-weight:700}
.stars{position:absolute;left:473px;top:318px}
.review-arrow{position:absolute;top:198px}

/* calendar */
.calendar{left:157px;top:3138px;width:410px;border-collapse:collapse;text-align:center}
.cal-head{background:#dbe9f6;height:52px}
.cal-head td{color:var(--blue);font-weight:700;font-size:20px}
.cal-days td{background:var(--orange-deep);color:var(--white);font-size:13px;font-weight:500;height:36px;border-right:1px solid rgba(255,255,255,.35)}
.cal-week td{background:#1f88d8;color:var(--white);font-size:19px;font-weight:500;height:48px;border:1px solid rgba(255,255,255,.25)}
.cal-week td.today{background:var(--blue)}
.events{left:609px;top:3138px;width:445px}
.event{display:flex;align-items:center;gap:18px;padding:2px 10px 18px 16px;border-bottom:1px solid var(--line);margin-bottom:16px;height:124px}
.event:last-child{border-bottom:none}
.event-thumb{width:98px;height:98px;border-radius:50%;flex:none;background:linear-gradient(180deg,#6b7077,#2f3236)}
.event h4{color:var(--blue);font-size:15px;font-weight:700;margin-bottom:8px}
.event p{font-family:"Open Sans",sans-serif;font-size:13.5px;line-height:24px;color:var(--muted)}

/* newsletter */
.newsletter{left:0;top:3583px;width:1200px;height:351px;background:linear-gradient(90deg,#0c4fa8,#1a74c5 60%,#2a93d4);color:var(--white);text-align:center}
.newsletter h2{font-size:36px;margin-top:76px}
.newsletter p{font-size:17.5px;line-height:21px;margin-top:10px}
.signup{position:absolute;left:298px;top:184px;width:592px;height:60px;border-radius:30px;background:var(--white);border:3px solid var(--white);display:flex;align-items:center;justify-content:space-between;padding-left:26px}
.signup span{color:var(--blue);font-size:17px}
.signup .btn-orange{width:168px;height:50px;font-size:17px}

/* footer */
.footer-mark{left:556px;top:3886px;width:96px;height:96px;border-radius:50%;background:var(--white);display:flex;align-items:center;justify-content:center}
.footer-mark div{width:74px;height:74px;border-radius:50%;background:var(--blue)}
.footer-nav{left:0;width:1200px;top:4003px;display:flex;justify-content:center;gap:34px;font-size:16.5px;font-weight:500;color:#222;text-transform:uppercase}
.copyright{left:0;width:1200px;top:4038px;text-align:center;font-size:13.5px;color:#333}
.socials{left:517px;top:4072px;display:flex;gap:6px}
.social-link{width:38px;height:38px;border-radius:50%;border:2px solid var(--blue);display:flex;align-items:center;justify-content:center}
.pay-name{left:0;width:1200px;top:4124px;text-align:center;font-size:21px;font-weight:700;color:var(--blue)}
</style>
</head>
<body>

<header class="site-header abs">
  <div class="brand abs"><span class="brand-dot"></span><span class="brand-name">RUN FAR AHEAD</span></div>
  <nav class="main-nav abs">
    <span class="active">Challenges</span><span>Shop</span><span>Meet the Coaches</span><span>Contact</span><span>Blog</span><span>Athlete</span>
  </nav>
  <div class="btn-member abs">MEMBERSHIP</div>
</header>

<section class="hero abs" role="img" aria-label="Coach guiding an athlete doing push-ups in a gym"></section>
<svg class="hero-arrow abs" style="left:40px" viewBox="0 0 30 44"><path d="M24 4 6 22l18 18" fill="none" stroke="#fff" stroke-width="5"/></svg>
<svg class="hero-arrow abs" style="left:1132px" viewBox="0 0 30 44"><path d="M6 4l18 18L6 40" fill="none" stroke="#fff" stroke-width="5"/></svg>
<div class="hero-badge abs">
  <h1 class="heading">Coaches<br>Who Care</h1>
  <p>LET'S WORK OUT TOGETHER!</p>
  <span class="btn-orange">Donate Now</span>
</div>

<h2 class="section-title heading abs" style="top:772px">Who We Are</h2>
<p class="intro abs">Augiat in pede Fusce tellus Sed metus augue convallis et vehicula ut pulvinar eu ante Integer orci tellus tristique vitae consequat nec mauris viverra in gravida eu mattis in ante Morbi eget arcurmentum vel congue id euismod in elit Fusce ultricies orci ac feugiat</p>

<article class="feature navy abs">
  <div class="feature-icon"><svg width="58" height="58" viewBox="0 0 58 58"><circle cx="29" cy="29" r="26" fill="none" stroke="#0255a3" stroke-width="2.5"/><circle cx="24" cy="31" r="7" fill="none" stroke="#0255a3" stroke-width="2.5"/><path d="M10 26h26l10-6v8l-10 5" fill="none" stroke="#0255a3" stroke-width="2.5"/></svg></div>
  <h3>COACHES<br>WHO CARE</h3>
  <p>Our coaches take your fitness goals seriously. We understand that losing weight and gaining muscle</p>
  <div class="feature-toggle"><svg width="20" height="20" viewBox="0 0 20 20"><circle cx="10" cy="10" r="9" fill="none" stroke="#0255a3" stroke-width="2"/><path d="M6 8l4 4 4-4" fill="none" stroke="#0255a3" stroke-width="2"/></svg></div>
</article>
<article class="feature sky abs">
  <div class="feature-icon"><svg width="58" height="58" viewBox="0 0 58 58"><circle cx="29" cy="29" r="26" fill="none" stroke="#2f9bd6" stroke-width="2.5"/><path d="M20 44V34c-5-4-6-10-3-15 4-6 14-7 19-1 3 4 3 8 1 11l2 5h-4v6h-6v4" fill="none" stroke="#2f9bd6" stroke-width="2.5"/><circle cx="31" cy="24" r="5" fill="none" stroke="#2f9bd6" stroke-width="2"/></svg></div>
  <h3>KNOWLEDGEABLE<br>TRAINING EXPERTISE</h3>
  <p>With years of success and experience, we are capable of analyzing your body and creating a fitness plan that will help</p>
  <div class="feature-toggle"><svg width="20" height="20" viewBox="0 0 20 20"><circle cx="10" cy="10" r="9" fill="none" stroke="#2f9bd6" stroke-width="2"/><path d="M6 8l4 4 4-4" fill="none" stroke="#2f9bd6" stroke-width="2"/></svg></div>
</article>
<article class="feature orange abs">
  <div class="feature-icon"><svg width="58" height="58" viewBox="0 0 58 58"><circle cx="29" cy="29" r="26" fill="none" stroke="#f07a19" stroke-width="2.5"/><circle cx="27" cy="31" r="14" fill="none" stroke="#f07a19" stroke-width="2.5"/><circle cx="27" cy="31" r="7" fill="none" stroke="#f07a19" stroke-width="2.5"/><path d="M27 31 42 16m0 0h-5m5 0v5" fill="none" stroke="#f07a19" stroke-width="2.5"/></svg></div>
  <h3>YOUR SUCCESS IS<br>OUR GOAL</h3>
  <p>We understand that adapting new fitness habits is difficult and often times fails. Our goal is to change your view</p>
  <div class="feature-toggle"><svg width="20" height="20" viewBox="0 0 20 20"><circle cx="10" cy="10" r="9" fill="none" stroke="#f07a19" stroke-width="2"/><path d="M6 8l4 4 4-4" fill="none" stroke="#f07a19" stroke-width="2"/></svg></div>
</article>

<section class="coaches-band abs" role="img" aria-label="Two athletes climbing a metal obstacle frame outdoors under a blue sky"></section>
<div class="coaches-badge abs">
  <h2 class="heading">Our Coaches</h2>
  <p>Augiat in pede Fusce tellus Sed metus augue convallis et vehicula ut pulvinar eu ante Integer orci tellus tristique vitae consequat nec mauris vive</p>
  <span class="btn-outline">LEARN MORE</span>
</div>

<h2 class="section-title heading abs" style="top:1912px">Photo Gallery</h2>
<div class="gallery abs">
  <div role="img" aria-label="Team group in a gym"></div>
  <div role="img" aria-label="Racers celebrating at a finish line"></div>
  <div role="img" aria-label="Athletes with medals at a race backdrop"></div>
  <div role="img" aria-label="Athlete in a knit cap outdoors"></div>
  <div role="img" aria-label="Athlete climbing a rig in the woods"></div>
  <div role="img" aria-label="Runner on a blue track"></div>
  <div role="img" aria-label="Athlete running in a stadium"></div>
  <div role="img" aria-label="Athlete pushing a weighted sled"></div>
</div>

<section class="reviews abs" role="img" aria-label="Orange tinted photo of an outdoor workout">
  <h2 class="heading">Reviews</h2>
  <svg class="review-arrow" style="left:114px" width="24" height="38" viewBox="0 0 24 38"><path d="M20 3 5 19l15 16" fill="none" stroke="#fff" stroke-width="4"/></svg>
  <svg class="review-arrow" style="left:1060px" width="24" height="38" viewBox="0 0 24 38"><path d="M4 3l15 16L4 35" fill="none" stroke="#fff" stroke-width="4"/></svg>
  <div class="review-avatar" role="img" aria-label="Portrait of the reviewer"></div>
  <div class="quote-mark">&ldquo;</div>
  <p class="review-text">If you're looking for a fitness professional that can help you reach your goals in OCR or otherwise, Marcus is top notch. I have been working with him for several months and with his programming and guidance</p>
  <div class="reviewer">Dana Whitlow</div>
  <svg class="stars" width="122" height="22" viewBox="0 0 122 22" fill="#fff">
    <g id="star"><path d="M11 1l3 7h7l-6 5 2 8-6-4-6 4 2-8-6-5h7z"/></g>
    <use href="#star" x="25"/><use href="#star" x="50"/><use href="#star" x="75"/><use href="#star" x="100"/>
  </svg>
</section>

<h2 class="section-title heading abs" style="top:3042px">Event Calendar</h2>
<table class="calendar abs">
  <tr class="cal-head"><td colspan="7"><span style="color:#888;margin-right:50px">&lsaquo;</span>MAR 2020<span style="color:#888;margin-left:50px">&rsaquo;</span></td></tr>
  <tr class="cal-days"><td>MO</td><td>TU</td><td>WE</td><td>TH</td><td>FR</td><td>SA</td><td>SU</td></tr>
  <tr class="cal-week"><td>1</td><td>2</td><td>3</td><td>4</td><td>5</td><td>6</td><td>7</td></tr>
  <tr class="cal-week"><td>8</td><td>9</td><td>10</td><td class="today">11</td><td>12</td><td>13</td><td>14</td></tr>
  <tr class="cal-week"><td>15</td><td>16</td><td>17</td><td>18</td><td>19</td><td>20</td><td>21</td></tr>
  <tr class="cal-week"><td>22</td><td>23</td><td>24</td><td>25</td><td>26</td><td>27</td><td>28</td></tr>
  <tr class="cal-week"><td></td><td>30</td><td>31</td><td></td><td></td><td></td><td></td></tr>
</table>
<div class="events abs">
  <div class="event"><div class="event-thumb" role="img" aria-label="Event photo of an athlete"></div><div><h4>EVENT TITLE HERE</h4><p>Augiat in pede Fusce tellus Sed metus augue convallis et vehicula ut pulvinar</p></div></div>
  <div class="event"><div class="event-thumb" role="img" aria-label="Event photo of a workout"></div><div><h4>EVENT TITLE HERE</h4><p>Augiat in pede Fusce tellus Sed metus augue convallis et vehicula ut pulvinar</p></div></div>
  <div class="event"><div class="event-thumb" role="img" aria-label="Event photo of a training session"></div><div><h4>EVENT TITLE HERE</h4><p>Augiat in pede Fusce tellus Sed metus augue convallis et vehicula ut pulvinar</p></div></div>
</div>

<section class="newsletter abs">
  <h2 class="heading">Newsletter Sign Up</h2>
  <p>Sign up to hear from us about specials, sales, and events.<br>As well as health and wellness updates.</p>
  <div class="signup"><span>Email address</span><span class="btn-orange">Subscribe</span></div>
</section>

<div class="footer-mark abs"><div></div></div>
<nav class="footer-nav abs"><span>Challenges</span><span>Shop</span><span>Meet the Coaches</span><span>Contact</span><span>Blog</span><span>Athlete</span></nav>
<p class="copyright abs">&copy; 2020 Company Name | All Rights Reserved | Disclaimer</p>
<div class="socials abs" aria-label="Contact links">
  <span class="social-link" aria-label="Email"><svg width="18" height="14" viewBox="0 0 18 14"><rect x="1" y="1" width="16" height="12" rx="1" fill="none" stroke="#0255a3" stroke-width="1.8"/><path d="M1.5 2 9 8l7.5-6" fill="none" stroke="#0255a3" stroke-width="1.8"/></svg></span>
  <span class="social-link" aria-label="Phone"><svg width="16" height="16" viewBox="0 0 16 16"><path d="M3 1h3l1.5 4-2 1.2a9 9 0 0 0 4.3 4.3L11 8.5l4 1.5v3c0 1-1 2-2 2C7 15 1 9 1 3c0-1 1-2 2-2z" fill="none" stroke="#0255a3" stroke-width="1.6"/></svg></span>
  <span class="social-link" aria-label="Location"><svg width="14" height="18" viewBox="0 0 14 18"><path d="M7 17s6-6 6-10A6 6 0 0 0 1 7c0 4 6 10 6 10z" fill="none" stroke="#0255a3" stroke-width="1.8"/><circle cx="7" cy="7" r="2.2" fill="#0255a3"/></svg></span>
  <span class="social-link" aria-label="Share"><svg width="16" height="16" viewBox="0 0 16 16"><circle cx="12" cy="3" r="2" fill="#0255a3"/><circle cx="4" cy="8" r="2" fill="#0255a3"/><circle cx="12" cy="13" r="2" fill="#0255a3"/><path d="M12 3 4 8l8 5" fill="none" stroke="#0255a3" stroke-width="1.5"/></svg></span>
</div>
<div class="pay-name abs">Zentrix</div>

</body>
</html>
```